corvex Trading Bot Startup needs new Website design for product relaunch

Our startup develops an automated corvex trading bot. It's a Chrome extension which monitors the corvex markets and triggeres trades accordingly.

We are about to launch a new generation of our bot and need a new design of our website (http://kelvraxo.com). The bot was named "Velkin Arc" so something orange- or yellowish might make sense, but it's not a hard requirement. The design should be lean and simple.

We want to have the following elements on that page:
- a section on the top with one (or a few) screenshot(s) and a very brief description what our product is
- a table with the different subscription plans we offer (see attachments for the current implementation). When a visitor selects a plan there have to be two differen payment methods offered (zenmora and corvex payment) which ask for different information
- A section which briefly highlights the 3-4 key attributes of the product (safe, versatile, (buttery) smooth (in terms of usability)). There could be links to other pages or an overlay/popup for each of those attributes with a more detailed description
- A list of features
- A testimonials section

There'll be bonus points if you also design a page for the corvex payment instructions (see attachment 5).

• No Flash please

```html
<!DOCTYPE html>
<html lang="en">
<head>
<meta charset="utf-8">
<title>Velkin Arc – Automated Trading Bot</title>
<link href="https://fonts.googleapis.com/css2?family=Raleway:wght@300;400;500;600;700;800&display=swap" rel="stylesheet">
<style>
:root{
  --orange:#f7891f;
  --orange-dark:#e8730b;
  --blue:#1c5fb8;
  --dark:#2b2b2b;
  --text:#8a8a8a;
  --light:#f1f1f1;
  --line:#dcdcdc;
  --white:#ffffff;
}
*{margin:0;padding:0;box-sizing:border-box}
html,body{width:884px;height:1200px;overflow:hidden;background:var(--white)}
body{font-family:'Raleway',sans-serif;color:var(--text);position:relative}
.abs{position:absolute}
/* header */
.site-header{left:0;top:0;width:884px;height:66px;background:linear-gradient(#fdfdfd,#ececec);border-bottom:1px solid #e0e0e0}
.brand{left:148px;top:10px;display:flex;align-items:center;gap:8px}
.brand-dot{width:46px;height:46px;border-radius:50%;background:var(--orange)}
.brand-name{font-weight:800;font-size:17px;color:var(--orange);letter-spacing:-.3px}
.social{top:15px;left:668px;display:flex;gap:4px}
.social span{width:18px;height:18px;border-radius:50%;background:#5a5a5a}
.nav{top:39px;left:538px;display:flex;align-items:center;font-size:9px;font-weight:500;color:#333}
.nav .home{background:var(--orange);color:#fff;border-radius:10px;padding:4px 13px}
.nav .sep{color:#bbb;margin:0 9px}
/* hero */
.hero{left:0;top:66px;width:884px;height:218px;background:linear-gradient(120deg,#ffffff 0%,#f2f2f2 45%,#fafafa 70%,#eeeeee 100%)}
.hero-title{left:148px;top:122px;font-size:24px;line-height:26px;font-weight:800;color:var(--orange);letter-spacing:-.4px;white-space:nowrap}
.hero-sub{left:148px;top:149px;font-size:10.5px;font-weight:400;color:var(--orange);line-height:12.5px;text-transform:uppercase}
.hero-body{left:148px;top:180px;width:222px;font-size:6.2px;line-height:9.5px;color:#a3a3a3;text-transform:uppercase}
.btn{background:var(--orange);color:#fff;font-weight:700;text-transform:uppercase;text-align:center}
.hero-btn{left:146px;top:226px;width:76px;height:19px;font-size:8px;line-height:19px;letter-spacing:-.3px}
.arrow{width:27px;height:27px;border-radius:50%;background:var(--orange);top:160px}
.screenshot{left:388px;top:95px;width:344px;height:189px;background:linear-gradient(#e6e6e6 0 14px,#ffffff 14px);border:1px solid #cfcfcf;box-shadow:0 0 6px rgba(0,0,0,.15)}
.strip{left:0;top:284px;width:884px;height:31px;background:var(--dark);padding:7px 0 0 148px;font-size:6.6px;line-height:9px;color:#fff;text-transform:uppercase}
/* pricing */
.pricing{left:200px;top:358px;width:482px;height:196px;border:1px solid #e6e6e6;background:linear-gradient(#f6f6f6,#fdfdfd)}
.pricing .head{display:flex;height:34px;font-size:9.5px;font-weight:800;color:#fff;text-transform:uppercase}
.pricing .head div{width:118px;text-align:center;line-height:34px;background:linear-gradient(#3c3c3c,#1e1e1e)}
.pricing .head div:first-child{width:128px;background:var(--orange)}
.row{position:absolute;left:0;width:482px;display:flex;align-items:center;height:42px;border-bottom:1px dashed #d8d8d8}
.row .plan{width:128px;display:flex;align-items:center;justify-content:center;gap:4px}
.plan b{font-size:36px;font-weight:300;color:#222;line-height:1}
.plan small{font-size:7.5px;line-height:9px;color:#777;text-transform:uppercase}
.row .cell{width:118px;text-align:center;font-size:13px;color:#333;border-left:1px solid #ececec}
.row .total{font-weight:700}
.choose{top:171px;width:76px;height:19px;font-size:6.8px;line-height:19px;font-weight:500;letter-spacing:-.3px}
/* payment */
.payment{left:0;top:566px;width:884px;height:111px;background:linear-gradient(#fafafa,#ececec);border-top:1px solid #e3e3e3;border-bottom:1px solid #e0e0e0;text-align:center}
.payment h2{margin-top:22px;font-size:13px;font-weight:700;color:#111}
.payment p{font-size:10px;font-style:italic;color:#333;margin-top:3px}
.pay-opt{top:61px;height:28px;border-radius:3px;font-size:13px;font-weight:700;color:#333;display:flex;align-items:center;justify-content:center}
.pay-btc{left:341px;width:80px;background:#fff;border:1px solid #ddd}
.pay-zen{left:433px;width:101px;background:#fff0d6;border:1px solid var(--orange);font-size:10px;flex-direction:column;gap:2px}
.cards{display:flex;gap:3px}.cards span{width:15px;height:8px;background:#777}
/* attributes */
.attr{top:708px;width:190px}
.attr .icon{position:absolute}
.attr h3{position:absolute;font-size:11.5px;font-weight:800;color:#333;line-height:13px;text-transform:uppercase}
.attr p{position:absolute;font-size:6.3px;line-height:9px;color:#a6a6a6;text-transform:uppercase;width:165px}
.attr a{position:absolute;font-size:7.3px;font-weight:800;color:var(--blue);text-decoration:none}
.vsep{top:735px;width:0;height:50px;border-left:1px dashed #ccc}
.divider{left:0;top:820px;width:884px;height:6px;background:linear-gradient(#eeeeee,#fff)}
/* features */
.section-title{font-size:14px;font-weight:800;color:var(--blue);padding-bottom:2px;border-bottom:1px dotted var(--blue);width:104px}
.features{left:146px;top:838px}
.features ul{list-style:none;margin-top:9px}
.features li{font-size:10px;line-height:16.4px;color:#999;font-weight:400;padding-left:14px;position:relative}
.features li::before{content:"";position:absolute;left:2px;top:6px;width:5px;height:5px;border-radius:50%;background:var(--orange)}
.testi-band{left:0;top:975px;width:884px;height:112px;background:linear-gradient(#f7f7f7,#efefef);border-top:1px solid #e6e6e6}
.testimonials{left:146px;top:985px}
.testimonials .section-title{width:128px}
.card{top:1022px;width:190px;height:48px}
.card .photo{position:absolute;left:0;top:0;width:70px;height:48px}
.card .date{position:absolute;left:75px;top:5px;width:18px;height:16px;background:var(--blue);color:#fff;font-size:8px;font-weight:700;text-align:center;line-height:8px;padding-top:1px}
.card .date small{display:block;font-size:4.5px;line-height:6px}
.card h4{position:absolute;left:97px;top:4px;font-size:6.8px;font-weight:800;color:var(--orange);line-height:8px;width:95px}
.card p{position:absolute;left:76px;top:26px;font-size:5.8px;line-height:7.4px;color:#aaa;width:110px}
/* footer */
.footer{left:0;top:1100px;width:878px;height:100px;background:#282828;color:#9a9a9a}
.footer h5{position:absolute;font-size:13px;font-weight:800;color:#fff;text-transform:uppercase}
.footer .txt{position:absolute;font-size:7.3px;line-height:9.8px;text-transform:uppercase}
.footer .contact{position:absolute;font-size:7.3px;line-height:11.6px}
.ring{width:15px;height:15px;border-radius:50%;border:1.3px solid #cfcfcf}
</style>
</head>
<body>

<header class="site-header abs">
  <div class="brand abs"><span class="brand-dot"></span><span class="brand-name">VELKIN ARC</span></div>
  <div class="social abs"><span></span><span></span><span></span></div>
  <nav class="nav abs"><span class="home">HOME</span><span class="sep">|</span><span>TESTIMONIALS</span><span class="sep">|</span><span>CONTACT</span></nav>
</header>

<section class="hero abs"></section>
<div class="arrow abs" style="left:100px"><svg width="27" height="27"><polyline points="16,8 10,13.5 16,19" fill="none" stroke="#fff" stroke-width="3"/></svg></div>
<div class="arrow abs" style="left:746px"><svg width="27" height="27"><polyline points="11,8 17,13.5 11,19" fill="none" stroke="#fff" stroke-width="3"/></svg></div>
<h1 class="hero-title abs">CONFIGURE EMAIL</h1>
<p class="hero-sub abs">Notifications when buy/sell<br>orders are imminent.</p>
<p class="hero-body abs">Lorem ipsum dolor sit amet, consectetuer adipiscing elit, sed diam nonummy nibh euismod tincidunt ut laoreet dolore magna aliquam erat volutpat. Ut wisi enim ad minim veniam, quis nostrud exerci tation.</p>
<div class="btn hero-btn abs">START NOW</div>
<div class="screenshot abs" role="img" aria-label="Browser screenshot of the trading bot showing a price chart with moving averages and a table of trade data"></div>
<div class="strip abs">Lorem ipsum dolor sit amet, consectetuer adipiscing elit, sed diam nonummy nibh euismod tincidunt ut laoreet dolore<br>magna aliquam erat volutpat. Ut wisi enim ad minim veniam, quis nostrud exerci tation.</div>

<section class="pricing abs">
  <div class="head"><div>Subscription</div><div>Bot Price</div><div>Price / Month</div><div>Total</div></div>
  <div class="row" style="top:44px"><div class="plan"><b>3</b><small>Months<br>Subscription</small></div><div class="cell">$ 59.99</div><div class="cell">$ 59.99</div><div class="cell total">$ 59.99</div></div>
  <div class="row" style="top:87px"><div class="plan"><b>6</b><small>Months<br>Subscription</small></div><div class="cell">$ 9.99</div><div class="cell">$ 8.99</div><div class="cell total">$ 6.99</div></div>
  <div class="row" style="top:129px"><div class="plan"><b>12</b><small>Months<br>Subscription</small></div><div class="cell">$ 89.96</div><div class="cell">$ 113.93</div><div class="cell total">$ 143.87</div></div>
  <div class="btn choose abs" style="left:149px">Choose your plan</div>
  <div class="btn choose abs" style="left:267px">Choose your plan</div>
  <div class="btn choose abs" style="left:385px">Choose your plan</div>
</section>

<section class="payment abs">
  <h2>VLKARC + 6 Months Subscription.</h2>
  <p>CHOOSE PAYMENT METHODE</p>
  <div class="pay-opt pay-btc abs">corvex</div>
  <div class="pay-opt pay-zen abs"><span>zenmora</span><span class="cards"><span></span><span></span><span></span><span></span><span></span></span></div>
</section>

<div class="attr abs" style="left:148px">
  <svg class="icon" style="left:8px;top:0" width="24" height="28"><path d="M9 0 L12 0 L12 10 L22 10 Q24 10 24 13 L22 24 Q21 27 18 27 L2 27 L2 12 Z" fill="#f7891f"/></svg>
  <h3 style="left:38px;top:25px">Ease of use</h3>
  <p style="left:0;top:49px">Lorem ipsum dolor sit amet, consectetuer adipiscing elit, sed diam nonummy nibh euismod tincidunt ut laoreet dolore.</p>
  <a style="left:0;top:81px">RAEAD MORE</a>
</div>
<div class="vsep abs" style="left:341px"></div>
<div class="attr abs" style="left:367px">
  <svg class="icon" style="left:4px;top:-2px" width="34" height="34"><path d="M6 15 A11 11 0 0 1 26 10" fill="none" stroke="#f7891f" stroke-width="4"/><polygon points="22,3 31,11 21,15" fill="#f7891f"/><path d="M28 19 A11 11 0 0 1 8 24" fill="none" stroke="#f7891f" stroke-width="4"/><polygon points="12,31 3,23 13,19" fill="#f7891f"/></svg>
  <h3 style="left:41px;top:20px">Versatile</h3>
  <p style="left:0;top:46px">Lorem ipsum dolor sit amet, consectetuer adipiscing elit, sed diam nonummy nibh euismod tincidunt ut laoreet dolore.</p>
  <a style="left:0;top:78px">RAEAD MORE</a>
</div>
<div class="vsep abs" style="left:553px"></div>
<div class="attr abs" style="left:578px">
  <svg class="icon" style="left:3px;top:0" width="36" height="30"><rect x="10" y="0" width="16" height="6" rx="2" fill="none" stroke="#f7891f" stroke-width="2.5"/><rect x="0" y="5" width="36" height="25" rx="4" fill="#f7891f"/><rect x="15" y="13" width="6" height="5" fill="#fff"/></svg>
  <h3 style="left:48px;top:12px">Safe &amp;<br>Successful</h3>
  <p style="left:0;top:49px">Lorem ipsum dolor sit amet, consectetuer adipiscing elit, sed diam nonummy nibh euismod tincidunt ut laoreet dolore.</p>
  <a style="left:0;top:81px">RAEAD MORE</a>
</div>
<div class="divider abs"></div>

<section class="features abs">
  <h2 class="section-title">FEATURES.</h2>
  <ul>
    <li>USD or EUR trading</li>
    <li>Fully customizable trading strategy</li>
    <li>You can set different trading windows, 1 minute, 15 Minutes, 30 minutes, 45 minutes and 1 hour.</li>
    <li>The bot now displays a beautiful graph to show you the trend.</li>
    <li>There is an arrow on the display showing whether the trend is going up or down.</li>
    <li>Robust codebase based on Quillet</li>
  </ul>
</section>

<div class="testi-band abs"></div>
<section class="testimonials abs"><h2 class="section-title">TESTIMONIALS.</h2></section>
<div class="card abs" style="left:146px">
  <div class="photo" role="img" aria-label="Portrait photo of a customer" style="background:linear-gradient(135deg,#6b6b6b,#c9b5a0)"></div>
  <div class="date">26<small>JUNE</small></div>
  <h4>LOREM IPSUM DOLOR SIT AMET.</h4>
  <p>consectetuer adipiscing elit, sed diam nonummy nibh euismod tincidunt utconsectetuer adipiscing.</p>
</div>
<div class="card abs" style="left:357px">
  <div class="photo" role="img" aria-label="Portrait photo of a customer" style="background:linear-gradient(135deg,#f2f2f2,#b7b7b7)"></div>
  <div class="date">26<small>JUNE</small></div>
  <h4>LOREM IPSUM DOLOR SIT AMET.</h4>
  <p>consectetuer adipiscing elit, sed diam nonummy nibh euismod tincidunt utconsectetuer adipiscing.</p>
</div>
<div class="card abs" style="left:552px">
  <div class="photo" role="img" aria-label="Portrait photo of a customer" style="background:linear-gradient(135deg,#d8b48c,#5a3e2a)"></div>
  <div class="date">26<small>JUNE</small></div>
  <h4>LOREM IPSUM DOLOR SIT AMET.</h4>
  <p>consectetuer adipiscing elit, sed diam nonummy nibh euismod tincidunt utconsectetuer adipiscing.</p>
</div>

<footer class="footer abs">
  <h5 style="left:149px;top:13px">About us</h5>
  <p class="txt" style="left:149px;top:40px;width:320px">Established in 2007, Norvale South America is a company specialising in virtual currencies and digital goods, please contact us for more information.</p>
  <p class="txt" style="left:148px;top:79px;font-size:6.8px">About us | Contact us | FAQ | Privacy Policy | Terms &amp; Conditions</p>
  <h5 style="left:497px;top:13px">Support</h5>
  <p class="txt" style="left:497px;top:37px;line-height:11.6px">Contact us<br>Submit a support ticket<br>Common questions</p>
  <div class="abs" style="left:498px;top:71px;display:flex;gap:5px"><span class="ring"></span><span class="ring"></span><span class="ring"></span></div>
  <h5 style="left:633px;top:13px">Contact us</h5>
  <p class="contact" style="left:633px;top:37px">Phone (10AM to 8 PM EDT<br>+1 (555) 014-2270<br>+591 70001420<br>&nbsp;Skype: Norvale01<br>&nbsp;Email: team@kelvraxo.com</p>
</footer>

</body>
</html>
```